New modern and colorful Brochure for Real Estate shop window/showcase

We are a real estate company in the swiss alps and we need a new design for our (very old fashioned) brochures. Our “word-doc” based “brochure” you’ll find in the attachment.

We need a whole new, modern, clean and colorful design. The key features of a property must be clearly visible, like: (Those key features must be editable)

- 1 main bigger picture of the property
- 4-6 small accompagning Fotos
- Floorplan
- Price
- Property Category
- Buildyear
- Number of rooms
- Number of bathrooms
- Number of bedrooms
- Squaremeter
- Parking place
- Specialities
- Very Short Descripton of the property

We put those brochures in our shop window/showcase, see foto in the attachment. In the attachment you’ll find our business card logo, letterhead logo and on our website www.halvormark-ag.ch another logo.

The new brochure will contain about 4-6 pictures with a main picture of the house, a floorplan and a short description. It must be clearly visible und readable from outside thru a window, so it canot be too small.

Format only A3 in LANDSCAPE.

It must be scalable to A4 to be able to send it to clients (and they will print it to A4)

The brochure must contain our logo with name, subname and year, website, telefon and fax number and address.

To be clear: The whole new brochure will contain only a short description, not like the old design. You can really more concentrate on design and fotos. Description and text will be very short. But we really want to change and no more using the old design...

Just to clarify, the picture with our little agency is just for reference where the new brochures will be. It's jus there to show our window/showcase.

Hope you can help us. Many Greetings and thank you from us!

Project Deadline Extended Reason: Not yet found/submitted "the one". We are missing a more central/important position of the key features of a property. They must be really clearly seen from outside of the window. And we need a two sided A4 "light" version, to hand out to clients. We can't give them a big A3 paper. Scaled down thru the printer isn't the best option. I light version would be optimal....Please continue to submit designs and adopt to the new task, we will reply and give immediate feedback. Thanks a lot! Added Tuesday, January 31, 2017

Reason: still not found the right one

Target Market(s)

Real Estate, Shop Window, Showcase

Industry/Entity Type

Real Estate

Font styles to use
Sans Serif

Colors
0655a3
ec1f27
0293ce
ffc214
e34297

Requirements
Must have
• A3 Format landscape.
• - 1 main bigger picture of the property
• - 4-6 small accompagning Fotos
• - Floorplan
• - Price
• - Property Category
• - Buildyear
• - Number of rooms
• - Number of bathrooms
• - Number of bedrooms
• - Squaremeter
• - Parking place
• - Specialities
• - Short Descripton of the property

```html
<!DOCTYPE html>
<html lang="de">
<head>
<meta charset="utf-8">
<title>2 ½-Zimmer Wohnung im Haus ALPINA – Exposé</title>
<link href="https://fonts.googleapis.com/css2?family=Lato:wght@300;400;700;900&display=swap" rel="stylesheet">
<style>
  :root {
    --blue-deep: #0b5c8c;
    --blue: #0a6a9c;
    --blue-panel: #0b70a3;
    --yellow: #ffc214;
    --red: #ec1f27;
    --white: #ffffff;
    --backdrop: #ececec;
    --snow-top: #c9d3df;
    --mountain: #5b6470;
  }
  * { box-sizing: border-box; margin: 0; padding: 0; }
  html, body { width: 1200px; height: 1000px; overflow: hidden; }
  body {
    background: var(--backdrop);
    font-family: "Lato", Arial, sans-serif;
    color: var(--white);
    position: relative;
  }
  .page {
    position: absolute;
    top: 173px;
    width: 438px;
    height: 617px;
    background: var(--blue-deep);
    overflow: hidden;
    border-bottom: 4px solid var(--red);
  }
  .page--front { left: 155px; }
  .page--back { left: 615px; }

  .hero-photo {
    position: absolute;
    left: 0; top: 0; width: 100%;
    background: linear-gradient(160deg, #b9c7d6 0%, #6f7884 30%, #4d5561 55%, #a9b2bd 75%, #e3e8ee 100%);
  }
  .page--front .hero-photo { height: 270px; }
  .page--back .hero-photo { height: 290px; }

  .wave { position: absolute; left: 0; width: 100%; }
  .page--front .wave { top: 190px; height: 120px; }
  .page--back .wave { top: 195px; height: 120px; }

  .house-photo {
    position: absolute;
    left: 274px; top: 116px;
    width: 142px; height: 142px;
    border-radius: 50%;
    border: 3px solid var(--white);
    background: linear-gradient(180deg, #8a7766 0%, #5d5048 45%, #9aa0a6 100%);
  }

  .title { position: absolute; left: 15px; top: 234px; width: 400px; }
  .title__rooms { font-size: 20px; font-weight: 900; line-height: 1.1; }
  .title__main { font-size: 21px; font-weight: 900; color: var(--yellow); line-height: 1.15; }
  .title__fr { font-size: 15px; font-weight: 300; line-height: 1.3; }
  .divider {
    position: absolute; left: 15px; top: 311px; width: 296px;
    border-top: 1px solid rgba(255,255,255,0.5);
  }

  .copy { position: absolute; left: 15px; top: 318px; width: 410px; font-size: 7px; line-height: 1.35; }
  .copy h2 { font-size: 7.5px; font-weight: 900; letter-spacing: 0.2px; margin-top: 4px; margin-bottom: 2px; }
  .copy h2 span { font-weight: 400; }
  .copy p { margin-bottom: 5px; }

  .facts {
    position: absolute; left: 33px; top: 435px; width: 370px; height: 104px;
    border: 1px solid rgba(255,255,255,0.7);
    background: var(--blue-panel);
    font-size: 7.5px; font-weight: 700;
  }
  .facts__row {
    display: grid;
    grid-template-columns: 86px 100px 100px 1fr;
    height: 29px; align-items: center; padding-left: 10px;
    border-bottom: 1px solid rgba(255,255,255,0.6);
  }
  .facts__row span b { font-weight: 900; }
  .facts__price {
    text-align: center; font-size: 25px; font-weight: 900; color: var(--yellow);
    line-height: 44px;
  }

  .brand { position: absolute; left: 15px; top: 560px; }
  .brand__name { display: flex; align-items: center; gap: 7px; font-size: 17px; font-weight: 900; letter-spacing: 0.5px; }
  .brand__dot { width: 28px; height: 28px; border-radius: 50%; background: var(--white); }
  .brand__sub { font-size: 10px; margin-left: 43px; margin-top: -6px; }
  .brand__tag { font-size: 9px; margin-top: 6px; }

  .contact {
    position: absolute; right: 10px; top: 560px;
    font-size: 7px; line-height: 1.3; text-align: right;
  }
  .contact b { font-weight: 900; }

  .gallery__item {
    position: absolute;
    border: 3px solid var(--white);
  }
  .g-village { left: 226px; top: 10px; width: 176px; height: 121px; background: linear-gradient(180deg, #7fa7d2 0%, #8b96a3 45%, #e7ebef 80%, #c4b8a8 100%); }
  .g-bed-a { left: 226px; top: 145px; width: 84px; height: 123px; background: linear-gradient(180deg, #e6e3dc 0%, #c9c4bb 55%, #8a5a3a 100%); }
  .g-bed-b { left: 318px; top: 145px; width: 84px; height: 123px; background: linear-gradient(180deg, #dcd8d1 0%, #bdb8b0 55%, #95603c 100%); }
  .g-living-a { left: 226px; top: 282px; width: 176px; height: 119px; background: linear-gradient(180deg, #a8845e 0%, #c9b9a3 40%, #8a4a2c 100%); }
  .g-living-b { left: 226px; top: 415px; width: 176px; height: 124px; background: linear-gradient(180deg, #a17b55 0%, #8c6a4c 45%, #6a3a28 100%); }

  .floorplan {
    position: absolute; left: 23px; top: 280px; width: 184px; height: 262px;
    background: var(--white);
  }
  .floorplan__area { position: absolute; inset: 10px 12px; background: #e4e4e4; }
</style>
</head>
<body>

<section class="page page--front">
  <div class="hero-photo" role="img" aria-label="Winter view of the snowy alpine valley with forested mountain slopes"></div>
  <svg class="wave" viewBox="0 0 438 120" preserveAspectRatio="none" aria-hidden="true">
    <path d="M0 30 C120 10 300 0 438 58 L438 120 L0 120 Z" fill="#ffc214"/>
    <path d="M0 38 C120 18 300 8 438 66 L438 120 L0 120 Z" fill="#0b5c8c"/>
  </svg>
  <div class="house-photo" role="img" aria-label="Facade of the apartment building with wooden balconies"></div>

  <header class="title">
    <h1 class="title__rooms">2 ½-Zimmer</h1>
    <p class="title__main">Wohnung im Haus ALPINA</p>
    <p class="title__fr">Appartement 2 ½ pièces dans l’immeuble ALPINA</p>
  </header>
  <div class="divider"></div>

  <div class="copy">
    <h2>BESCHREIBUNG <span>DESCRIPTION</span></h2>
    <p>Die renovierte und modernisierte 2 ½-Zimmer-Wohnung verfügt über den rückseitigen Grundriss, ist komplett möbliert und eingerichtet und kann sofort oder nach Vereinbarung übernommen und genutzt werden. Zur Wohnung gehören ein grundbuchrechtlich abgesicherter Autoabstellplatz in der Halle und ein Abstellraum.</p>
    <p>L’appartement de 2 ½ pièces disposé sur le plan au verso, est complètement meublé, équipé et peut être utilisé de suite ou selon entente. Avec l’appartement, il y a également une place de parc dans le garage inscrite au registre foncier et un local de rangement.</p>
    <h2>BESONDERHEITEN <span>PARTICULARITÉS</span></h2>
    <p>Erwerb durch Nichtschweizer möglich Achat possible par des étrangers</p>
  </div>

  <div class="facts">
    <div class="facts__row">
      <span>Rooms:&nbsp; 2 ½</span><span>Bathrooms:&nbsp; 1</span><span>Bedrooms:&nbsp; 2</span><span>Parking:&nbsp; 1</span>
    </div>
    <div class="facts__row">
      <span>Buildyear:&nbsp; 1972</span><span>Squaremeter:&nbsp; 80</span><span style="grid-column: span 2">Property Category:&nbsp; Haus</span>
    </div>
    <div class="facts__price">CHF 210'000</div>
  </div>

  <div class="brand">
    <div class="brand__name"><span class="brand__dot"></span>HALVORMARK AG</div>
    <div class="brand__sub">Immobilien und Finanzierungen</div>
    <div class="brand__tag">Seit 1980 | Erfahrung | Vertrauen | Kompetenz</div>
  </div>
  <address class="contact" style="font-style:normal">
    <b>HALVORMARK AG</b><br>3999 Bergdorf<br>
    <b>Telefon</b>: +41 27 555 01 10<br>
    <b>Telefax</b>: +41 27 555 01 11<br>
    <b>E-Mail</b>: kontakt@halvormark-ag.ch<br>
    <b>Internet</b>: http://www.halvormark-ag.ch
  </address>
</section>

<section class="page page--back">
  <div class="hero-photo" role="img" aria-label="Snowy mountain valley panorama"></div>
  <svg class="wave" viewBox="0 0 438 120" preserveAspectRatio="none" aria-hidden="true">
    <path d="M0 70 C150 30 320 8 438 6 L438 120 L0 120 Z" fill="#ffc214"/>
    <path d="M0 78 C150 38 320 16 438 14 L438 120 L0 120 Z" fill="#0b5c8c"/>
  </svg>

  <div class="gallery__item g-village" role="img" aria-label="Village in the snow under a blue sky"></div>
  <div class="gallery__item g-bed-a" role="img" aria-label="Bedroom with single bed"></div>
  <div class="gallery__item g-bed-b" role="img" aria-label="Second view of the bedroom"></div>
  <div class="gallery__item g-living-a" role="img" aria-label="Living and dining room with wooden ceiling"></div>
  <div class="gallery__item g-living-b" role="img" aria-label="Living room with sofa and wardrobe"></div>

  <div class="floorplan">
    <div class="floorplan__area" role="img" aria-label="Floor plan: hallway, bathroom, kitchen, bedroom, living and dining room, balcony"></div>
  </div>

  <div class="brand">
    <div class="brand__name"><span class="brand__dot"></span>HALVORMARK AG</div>
    <div class="brand__sub">Immobilien und Finanzierungen</div>
    <div class="brand__tag">Seit 1980 | Erfahrung | Vertrauen | Kompetenz</div>
  </div>
  <address class="contact" style="font-style:normal">
    <b>HALVORMARK AG</b><br>3999 Bergdorf<br>
    <b>Telefon</b>: +41 27 555 01 10<br>
    <b>Telefax</b>: +41 27 555 01 11<br>
    <b>E-Mail</b>: kontakt@halvormark-ag.ch<br>
    <b>Internet</b>: http://www.halvormark-ag.ch
  </address>
</section>

</body>
</html>
```